Design for Pediatric Occupational Therapist who works with children with special needs

I need 2 x 2 sq business cards and post cards for my Pediatric Occupational Therapy business. We work with children with special needs and help them learn skills for daily living (eating, writing, dressing, etc). We're looking for a colorful design (not loud) that looks professional and helps it stand out from other cards. I want to avoid many of the standard designs that you see on Nimbo press which are used my many other Pediatric OT's. The design will be intended for business cards, post cards and hopefully can also be used on company letterhead. I'll upload a current copy of the logo we currently use on company letter head so you get an idea of the design we've been using to date. This image does not need to be used again, but serves more as a reference to the design used in the past. The winning designer will likely be hired to design a custom logo for letter head.
Updates

Project Deadline Extended Reason: I want to extend the deadline to allow for more designs and review time. Added Sunday, January 8, 2017

Target Market(s)

Families of children with special needs, pediatricians

Industry/Entity Type

Business

Contact Information for Business Card

I need a logo or design for 2 x 2 sq business cards and post cards for my Pediatric Occupational Therapy business. We work with children with special needs and help them learn skills for daily living (eating, writing, dressing, etc). We're looking for a colorful design (not loud) that looks professional and helps it stand out from other cards. I want to avoid many of the standard designs that you see on Nimbo press which are used my many other Pediatric OT's. The design will be intended for business cards, post cards and hopefully can also be used on company letterhead. I'll upload a current copy of the logo we currently use on company letter head so you get an idea of the design we've been using to date.

Font styles to use
Sans Serif

Requirements
Must have
• Area to include company name, address, phone, etc.
• Company name = Meadowlark Therapy Partners

```html
<!DOCTYPE html>
<html lang="en">
<head>
<meta charset="utf-8">
<title>Pediatric Therapy Square Business Card</title>
<link rel="stylesheet" href="https://fonts.googleapis.com/css2?family=Bebas+Neue&family=Arimo:wght@400;700&family=PT+Sans&display=swap">
<style>
  :root {
    --stage: #000000;
    --navy: #0a3a5e;
    --sky: #29a8e0;
    --silver: #a9a7aa;
    --paper: #ffffff;
    --magenta: #d6177f;
    --ink: #111111;
  }
  html, body {
    margin: 0;
    width: 1200px;
    height: 999px;
    overflow: hidden;
    background: var(--stage);
  }
  .canvas { position: relative; width: 1200px; height: 999px; }
  .card {
    position: absolute;
    width: 558px;
    height: 558px;
    overflow: hidden;
  }
  .card--front { left: 27px; top: 256px; background: var(--paper); }
  .card--back  { left: 611px; top: 261px; background: var(--navy); }
  .card__art { position: absolute; inset: 0; }
  .front-text { position: absolute; left: 0; width: 100%; text-align: center; margin: 0; }
  .company-name {
    top: 30px;
    font-family: "Bebas Neue", sans-serif;
    font-size: 88px;
    line-height: 82px;
    color: var(--magenta);
    letter-spacing: 1px;
  }
  .person-name {
    top: 220px;
    font-family: "Arimo", sans-serif;
    font-weight: 700;
    font-size: 32px;
    color: var(--ink);
  }
  .designation {
    top: 264px;
    font-family: "Arimo", sans-serif;
    font-size: 22px;
    color: var(--ink);
  }
  .contact {
    top: 354px;
    font-family: "PT Sans", sans-serif;
    font-size: 24px;
    line-height: 32px;
    color: var(--paper);
  }
  .contact__group { margin: 0 0 18px; }
  .kids-illustration {
    position: absolute;
    left: 44px;
    top: 234px;
    width: 475px;
    height: 97px;
    border-radius: 12px;
    background: linear-gradient(90deg, #7bc24f, #e2403f, #2a9fd6, #d6177f, #f5a623, #3aa655, #7fcde8, #8a4fb0, #c763a8);
    opacity: 0.55;
  }
</style>
</head>
<body>
<main class="canvas">
  <section class="card card--front">
    <svg class="card__art" viewBox="0 0 558 558" aria-hidden="true">
      <path d="M558,181 C450,258 330,305 200,326 Q380,320 558,246 Z" fill="var(--sky)"/>
      <path d="M0,264 Q270,380 558,246 L558,558 L0,558 Z" fill="var(--silver)"/>
      <path d="M0,272 Q270,388 558,254 L558,558 L0,558 Z" fill="var(--navy)"/>
    </svg>
    <h1 class="front-text company-name">Company<br>Name</h1>
    <p class="front-text person-name">Person Name</p>
    <p class="front-text designation">Designation</p>
    <address class="front-text contact">
      <p class="contact__group">suit # 00, Lorem ipsum<br>Lorem Lorem ipsum</p>
      <p class="contact__group">Tel: 000-000-0000<br>Email: abcde@abcdef.com<br>Web: www.abcdef.com</p>
    </address>
  </section>

  <section class="card card--back">
    <svg class="card__art" viewBox="0 0 558 558" aria-hidden="true">
      <path d="M0,176 Q290,70 558,200 L558,372 Q260,490 0,386 Z" fill="var(--silver)"/>
      <path d="M0,184 Q290,80 558,210 L558,364 Q260,480 0,378 Z" fill="var(--sky)"/>
      <path d="M0,238 Q320,90 558,210 L558,300 Q250,500 0,378 Z" fill="var(--paper)"/>
    </svg>
    <div class="kids-illustration" role="img" aria-label="Illustration of a row of cartoon children holding hands"></div>
  </section>
</main>
</body>
</html>
```